Personal Injury Law Firm Marketing Postcards

Looking for 4 different high quality graphic postcards (print on both sides of 4"x6" postcard to market a Personal Injury Lawyer (Walter Dunmore). These will be placed on cars and in stores on stands. My photo and/or stock images.... We are targeting People who have been injured in automobile accidents, motorcycle accidents, slip and fall (wet/greasy floors indoors in supermarkets, restaurants, etc., snow and ice outdoors on sidewalks) trip and fall cases on dangerous staircases. indoor/outdoor, dog bite injuries. ( I like the use of stock images of these type of injury causing accidents. You can use following language "Serving People Injured in NY & NJ" . Millions of Dollars Recovered, Free Consultation and No Fee Unless We Recover Money! Phone number to be displayed (555) 614-3082 "call or text" Available 24 hours a day 7 days per week. May also want to mention that we can take over your case from another lawyer if you are not satisfied with your current attorney. There should be a small space in corner which has a space for my marketing person to handwrite in their reference code.

Target Market(s)

18-75 years old - densely populated major city

Industry/Entity Type

Legal

Font styles to use
Other font styles liked:
• Please use logo style that I uploaded.. Please do not just cut parts of my website out and use them. Do not use LOGO from my website

Colors
0054AA
0677BA
7BADD7
CADEEF
E8F1F8
00AB8E
00BBA5
67D7C9
C6EFE9
E9F9F6

Requirements
Must have
• Professional Appearance

```html
<!DOCTYPE html>
<html lang="en">
<head>
<meta charset="utf-8">
<title>Walter Dunmore Postcard – Front and Back</title>
<link href="https://fonts.googleapis.com/css2?family=Montserrat:ital,wght@0,400;0,500;0,600;0,700;0,800;1,400&display=swap" rel="stylesheet">
<style>
  :root {
    --gold: #c9a85c;
    --gold-deep: #b8964a;
    --black: #0d0d0d;
    --white: #ffffff;
    --ink: #111111;
    --page: #f0f0f0;
    --photo-dark: #2f241d;
    --photo-mid: #6a4c37;
  }
  * { box-sizing: border-box; margin: 0; padding: 0; }
  html, body { width: 1200px; height: 1200px; overflow: hidden; }
  body {
    background: var(--page);
    font-family: "Montserrat", Arial, sans-serif;
    color: var(--ink);
    position: relative;
  }
  .postcard {
    position: absolute;
    left: 196px;
    width: 808px;
    height: 538px;
    background: var(--white);
    overflow: hidden;
    box-shadow: 0 6px 18px rgba(0,0,0,.18);
  }
  .postcard--front { top: 44px; }
  .postcard--back { top: 616px; }
  .layer { position: absolute; left: 0; top: 0; }
  .abs { position: absolute; }

  /* Front */
  .firm-mark {
    left: 40px; top: 70px; width: 220px;
    text-align: center; color: var(--gold); font-weight: 600;
  }
  .firm-mark__square { width: 46px; height: 46px; border: 3px solid var(--gold); margin: 0 auto 14px; }
  .firm-mark__small { font-size: 12px; letter-spacing: 1px; }
  .firm-mark__name { font-size: 22px; letter-spacing: .5px; line-height: 1.2; }
  .firm-mark__suffix { font-size: 11px; }

  .portrait {
    left: 279px; top: 34px; width: 138px; height: 238px;
    background: linear-gradient(180deg, #4b505c 0%, #2a2f3b 60%, #1f2430 100%);
    border-radius: 40px 40px 0 0;
  }
  .offer-band {
    left: 0; top: 272px; width: 454px; height: 112px;
    background: var(--black); color: var(--white);
    padding: 12px 0 0 38px;
  }
  .offer__lead { font-size: 19px; font-weight: 400; }
  .offer__title { font-size: 34px; font-weight: 700; line-height: 1.15; }
  .offer-band .offer__title { color: var(--gold); }
  .offer__sub { font-size: 16.5px; font-weight: 400; }

  .case-list { list-style: none; font-size: 18px; line-height: 23px; }
  .postcard--front .case-list { left: 38px; top: 403px; color: var(--ink); }

  .phone-pill {
    left: 444px; top: 34px; width: 364px; height: 50px;
    background: var(--gold); border-radius: 25px 0 0 25px;
    display: flex; align-items: center;
  }
  .phone-pill__icon {
    width: 50px; height: 50px; border-radius: 50%;
    background: var(--black); display: flex; align-items: center; justify-content: center;
  }
  .phone-pill__number { font-size: 30px; font-weight: 700; color: var(--black); margin-left: 22px; }

  .region-strip {
    left: 497px; top: 469px; width: 311px; height: 37px;
    background: var(--white);
    display: flex; align-items: center; padding-left: 26px;
    font-size: 16.5px; font-weight: 500; gap: 10px;
  }

  /* Back */
  .back-mark {
    left: 404px; top: 100px; width: 200px; text-align: center;
    color: var(--gold); font-weight: 600; font-size: 12px; line-height: 15px;
  }
  .back-mark__square { width: 18px; height: 18px; border: 2px solid var(--gold); margin: 0 auto 6px; }
  .stamp-box { left: 675px; top: 32px; width: 92px; height: 105px; border: 2px solid var(--black); }
  .address-line { left: 500px; width: 266px; height: 2px; background: var(--black); }

  .back-offer { left: 35px; top: 206px; color: var(--ink); }
  .back-offer .offer__title { color: var(--black); font-weight: 800; }
  .postcard--back .case-list {
    left: 35px; top: 314px; color: var(--white); font-style: italic;
    font-size: 17.5px; line-height: 20.5px;
  }
  .contact-row { left: 35px; display: flex; align-items: center; gap: 10px; }
  .contact-row--phone { top: 424px; font-size: 24px; font-weight: 700; }
  .contact-row--region { top: 462px; font-size: 18px; font-weight: 400; }
</style>
</head>
<body>

<section class="postcard postcard--front" aria-label="Postcard front">
  <svg class="layer" width="808" height="538" viewBox="0 0 808 538" aria-hidden="true">
    <defs>
      <linearGradient id="justiceTone" x1="0" y1="0" x2="1" y2="1">
        <stop offset="0" stop-color="#1c1a1a"/>
        <stop offset=".5" stop-color="#5a4030"/>
        <stop offset="1" stop-color="#2a1f19"/>
      </linearGradient>
    </defs>
    <path d="M600 0 C455 95 398 330 492 538 L808 538 L808 0 Z" fill="var(--gold)"/>
    <path d="M618 0 C475 98 418 330 510 538 L808 538 L808 0 Z" fill="url(#justiceTone)"/>
  </svg>
  <div class="abs" role="img" aria-label="Photo of a bronze Lady Justice statue with scales and a wooden gavel"
       style="left:600px;top:120px;width:1px;height:1px;"></div>

  <div class="abs firm-mark">
    <div class="firm-mark__square"></div>
    <div class="firm-mark__small">LAW OFFICE OF</div>
    <div class="firm-mark__name">WALTER DUNMORE</div>
    <div class="firm-mark__suffix">P.C.</div>
  </div>

  <div class="abs portrait" role="img" aria-label="Portrait photo of attorney Walter Dunmore in a dark suit"></div>

  <div class="abs offer-band">
    <p class="offer__lead">Millions of Dollars Recovered</p>
    <p class="offer__title">Free Consultation</p>
    <p class="offer__sub">and No Fee Unless We Recover Money!</p>
  </div>

  <ul class="abs case-list">
    <li>Automobile accidents</li>
    <li>Motorcycle accidents</li>
    <li>Slip and fall (wet / greasy floors</li>
    <li>Indoors in supermarkets, restaurants, etc...</li>
  </ul>

  <div class="abs phone-pill">
    <div class="phone-pill__icon">
      <svg width="26" height="26" viewBox="0 0 24 24" aria-hidden="true">
        <circle cx="12" cy="12" r="10.5" fill="none" stroke="#fff" stroke-width="1.6"/>
        <path d="M8.6 7.2l1.6-.4 1 2.3-1 .8c.5 1.2 1.4 2.1 2.6 2.7l.8-1 2.3 1-.4 1.6c-3.6.2-7.1-3.3-6.9-7z" fill="#fff"/>
      </svg>
    </div>
    <span class="phone-pill__number">(555) 614-3082</span>
  </div>

  <div class="abs region-strip">
    <span>New Jersey and New York</span>
    <svg width="14" height="16" viewBox="0 0 14 16" aria-hidden="true">
      <circle cx="7" cy="5" r="3.2" fill="none" stroke="var(--gold)" stroke-width="1.8"/>
      <path d="M1.5 15c.8-3 3-4.5 5.5-4.5s4.7 1.5 5.5 4.5" fill="none" stroke="var(--gold)" stroke-width="1.8"/>
    </svg>
  </div>
</section>

<section class="postcard postcard--back" aria-label="Postcard back">
  <svg class="layer" width="808" height="538" viewBox="0 0 808 538" aria-hidden="true">
    <defs>
      <linearGradient id="gavelTone" x1="0" y1="0" x2="1" y2="1">
        <stop offset="0" stop-color="#2a1d15"/>
        <stop offset=".6" stop-color="#6b4a32"/>
        <stop offset="1" stop-color="#3a2a20"/>
      </linearGradient>
    </defs>
    <rect x="0" y="0" width="380" height="210" fill="url(#gavelTone)" role="img" aria-label="Photo of a wooden gavel in front of law books"/>
    <circle cx="491" cy="46" r="192" fill="var(--white)"/>
    <circle cx="491" cy="46" r="169" fill="var(--black)"/>
    <circle cx="179" cy="359" r="269" fill="var(--gold)"/>
  </svg>

  <div class="abs back-mark">
    <div class="back-mark__square"></div>
    <div>LAW OFFICE OF</div>
    <div>WALTER DUNMORE</div>
  </div>

  <div class="abs stamp-box"></div>
  <div class="abs address-line" style="top:363px"></div>
  <div class="abs address-line" style="top:411px"></div>
  <div class="abs address-line" style="top:459px"></div>

  <div class="abs back-offer">
    <p class="offer__lead">Millions of Dollars Recovered</p>
    <p class="offer__title">Free Consultation</p>
    <p class="offer__sub">and No Fee Unless We Recover Money!</p>
  </div>

  <ul class="abs case-list">
    <li>Automobile accidents</li>
    <li>Motorcycle accidents</li>
    <li>Slip and fall (wet / greasy floors</li>
    <li>Indoors in supermarkets, restaurants, etc...</li>
  </ul>

  <div class="abs contact-row contact-row--phone">
    <svg width="20" height="20" viewBox="0 0 24 24" aria-hidden="true">
      <circle cx="12" cy="12" r="10.5" fill="none" stroke="var(--black)" stroke-width="2"/>
      <path d="M8.6 7.2l1.6-.4 1 2.3-1 .8c.5 1.2 1.4 2.1 2.6 2.7l.8-1 2.3 1-.4 1.6c-3.6.2-7.1-3.3-6.9-7z" fill="var(--black)"/>
    </svg>
    <span>(555) 614-3082</span>
  </div>
  <div class="abs contact-row contact-row--region">
    <svg width="14" height="16" viewBox="0 0 14 16" aria-hidden="true">
      <circle cx="7" cy="5" r="3.2" fill="none" stroke="var(--black)" stroke-width="1.8"/>
      <path d="M1.5 15c.8-3 3-4.5 5.5-4.5s4.7 1.5 5.5 4.5" fill="none" stroke="var(--black)" stroke-width="1.8"/>
    </svg>
    <span>New Jersey and New York</span>
  </div>
</section>

</body>
</html>
```